Brennick Holdings Business Cards

These are professional business cards that are for my family office.
Put fake emails and phone numbers as of now until I finalize those components. This family office controls my families investments, assets, and future. The cards should be professional.
..
.
.
.
I just uploaded another variation of a logo I would like to see as a business card to I am inbeteen which logo to use

Target Market(s)

business

Industry/Entity Type

business

Contact Information for Business Card

Professional, wealth related, finance related.

Requirements
Must have
• Logo

```html
<!DOCTYPE html>
<html lang="en">
<head>
<meta charset="utf-8">
<title>Brennick Holdings Business Cards</title>
<link rel="stylesheet" href="https://fonts.googleapis.com/css2?family=Cinzel:wght@400;600&family=Montserrat:wght@400;700&display=swap">
<style>
  :root {
    --backdrop: #b9b9b9;
    --card: #060606;
    --ink: #ffffff;
    --ink-soft: #d6d6d6;
    --pattern-dark: #0b0b0b;
    --pattern-light: #3a3a3a;
  }
  * { box-sizing: border-box; margin: 0; padding: 0; }
  html, body { width: 1200px; height: 721px; overflow: hidden; }
  body {
    background: var(--backdrop);
    position: relative;
    font-family: "Montserrat", sans-serif;
    color: var(--ink);
  }
  .card {
    position: absolute;
    width: 500px;
    height: 286px;
    border-radius: 16px;
    background: var(--card);
    overflow: hidden;
  }
  .card--back { left: 70px; top: 120px; }
  .card--front { left: 630px; top: 315px; }

  .pattern-field {
    position: absolute;
    inset: 0;
    background: linear-gradient(120deg, var(--pattern-light) 0%, var(--pattern-dark) 70%);
  }
  .wordmark {
    font-family: "Cinzel", serif;
    font-weight: 400;
    letter-spacing: 0.04em;
    color: var(--ink);
    white-space: nowrap;
  }
  .card--back .wordmark {
    position: absolute;
    right: 34px;
    bottom: 96px;
    font-size: 22px;
  }

  .brand-mark {
    position: absolute;
    left: 78px;
    top: 88px;
    width: 124px;
    height: 124px;
    border: 3px solid var(--ink);
    border-radius: 50%;
  }

  .divider {
    position: absolute;
    left: 262px;
    top: 64px;
    height: 150px;
    width: 1.5px;
    background: var(--ink);
  }
  .details {
    position: absolute;
    left: 288px;
    top: 62px;
  }
  .details .wordmark { font-size: 17px; margin-bottom: 14px; }
  .details__name {
    font-weight: 700;
    font-size: 17px;
    letter-spacing: 0.02em;
  }
  .details__role {
    font-size: 12px;
    color: var(--ink-soft);
    margin-bottom: 12px;
  }
  .contact-line {
    display: flex;
    align-items: center;
    gap: 6px;
    font-size: 11.5px;
    color: var(--ink-soft);
    margin-bottom: 5px;
  }
  .contact-line svg { width: 11px; height: 11px; fill: var(--ink); flex: none; }
</style>
</head>
<body>
  <section class="card card--back">
    <div class="pattern-field" role="img" aria-label="Repeating monogram pattern in black and dark grey"></div>
    <p class="wordmark">Brennick Holdings</p>
  </section>

  <section class="card card--front">
    <div class="brand-mark" aria-hidden="true"></div>
    <div class="divider"></div>
    <div class="details">
      <p class="wordmark">Brennick Holdings</p>
      <p class="details__name">ADRIAN VALE</p>
      <p class="details__role">Founder</p>
      <p class="contact-line">
        <svg viewBox="0 0 24 24" aria-hidden="true"><path d="M6.6 10.8a15 15 0 0 0 6.6 6.6l2.2-2.2c.3-.3.7-.4 1-.2 1.1.4 2.3.6 3.6.6.6 0 1 .4 1 1V20c0 .6-.4 1-1 1A17 17 0 0 1 3 4c0-.6.4-1 1-1h3.5c.6 0 1 .4 1 1 0 1.3.2 2.5.6 3.6.1.3 0 .7-.2 1z"/></svg>
        555-201-4470
      </p>
      <p class="contact-line">
        <svg viewBox="0 0 24 24" aria-hidden="true"><path d="M2 5h20v14H2zm2 2v.5l8 5 8-5V7l-8 5z"/></svg>
        office@brennickmail.com
      </p>
    </div>
  </section>
</body>
</html>
```